Landscape design build company door flyer

I would like this flyer to convey a high-level of professionalism for a company that is excellent with communication with their clients as well as a company that does incredible installations

Went on vacation/holiday

```html
<!DOCTYPE html>
<html lang="en">
<head>
<meta charset="UTF-8">
<title>Cedar Builders – Landscape Flyer</title>
<link href="https://fonts.googleapis.com/css2?family=Montserrat:wght@500;600;700;800&display=swap" rel="stylesheet">
<style>
  :root {
    --navy: #0d3349;
    --leaf: #07870d;
    --hedge-dark: #1f7a12;
    --hedge-mid: #3fa51c;
    --hedge-light: #7cc63a;
    --sun: #fff3d6;
    --bush-dark: #1e5a22;
    --bush-mid: #3d8a2c;
    --white: #ffffff;
  }
  * { margin: 0; padding: 0; box-sizing: border-box; }
  html, body { width: 848px; height: 1200px; overflow: hidden; background: var(--white); }
  body { font-family: "Montserrat", sans-serif; }

  .flyer { position: relative; width: 848px; height: 1200px; overflow: hidden; background: var(--white); }

  .bush-photo {
    position: absolute; left: 0; top: 355px; width: 848px; height: 720px;
    background: radial-gradient(ellipse at 85% 60%, var(--bush-mid) 0%, var(--bush-dark) 55%, #1b4a2c 100%);
  }

  .hedge-photo {
    position: absolute; left: 0; top: 0; width: 848px; height: 540px;
    clip-path: polygon(0 0, 100% 0, 100% 360px, 0 520px);
    background:
      radial-gradient(circle at 88% 12%, var(--sun) 0%, rgba(255,230,170,0.7) 12%, rgba(255,220,150,0) 34%),
      linear-gradient(100deg, var(--hedge-dark) 0%, var(--hedge-mid) 35%, var(--hedge-light) 60%, #9fcf5a 80%, #e9e2c4 100%);
  }

  .navy-panel {
    position: absolute; left: 0; top: 355px; width: 848px; height: 720px;
    clip-path: polygon(0 165px, 100% 5px, 100% 100%, 0 100%);
    background: linear-gradient(90deg, var(--navy) 0%, var(--navy) 44%, rgba(13,51,73,0.75) 58%, rgba(13,51,73,0.15) 85%, rgba(13,51,73,0) 100%);
  }

  .divider { position: absolute; left: 0; top: 0; width: 848px; height: 1200px; pointer-events: none; }

  .gallery-photo {
    position: absolute; width: 210px; height: 210px; border-radius: 50%;
    border: 5px solid var(--white);
  }
  .gallery-photo--pool { left: 76px; top: 353px; background: radial-gradient(circle at 55% 50%, #4cc3d9 0%, #6fb84a 45%, #d9ddd8 100%); }
  .gallery-photo--courtyard { left: 319px; top: 287px; background: linear-gradient(180deg, #c8d8c0 0%, #4f8a3a 40%, #8a8a80 75%, #5f9b3a 100%); }
  .gallery-photo--shrubs { left: 558px; top: 252px; background: linear-gradient(160deg, #e7c58a 0%, #6fae3a 45%, #3f8a24 75%, #86c93c 100%); }

  .brand-name {
    position: absolute; left: 601px; top: 96px; width: 240px; text-align: center;
    font-weight: 700; font-size: 18px; letter-spacing: 0.5px; color: var(--navy);
  }

  .section-label {
    position: absolute; left: 91px; height: 37px; padding: 0 12px 0 11px;
    background: var(--leaf); color: var(--white);
    font-weight: 800; font-size: 20px; letter-spacing: 2px; line-height: 37px;
    border-top-right-radius: 10px;
  }
  .section-label--about { top: 632px; }
  .section-label--services { top: 861px; }

  .section-text {
    position: absolute; left: 91px; width: 676px;
    color: var(--white); font-weight: 500; font-size: 18.5px; line-height: 28.6px;
    letter-spacing: 1.9px; text-align: justify; text-align-last: left;
  }
  .section-text--about { top: 695px; }
  .section-text--services { top: 923px; }

  .contact-band {
    position: absolute; left: 0; top: 1077px; width: 848px; height: 46px;
    background: var(--leaf); color: var(--white);
    font-weight: 800; font-size: 27px; letter-spacing: 3.5px; text-align: center; line-height: 46px;
  }

  .contact-line {
    position: absolute; top: 1148px; height: 28px; display: flex; align-items: center; gap: 8px;
    font-weight: 700; font-size: 19.5px; letter-spacing: 0.6px; color: var(--navy); white-space: nowrap;
  }
  .contact-line svg { flex: none; }
  .contact-line--phone { left: 34px; }
  .contact-line--email { left: 239px; }
  .contact-line--web { left: 486px; gap: 11px; }
</style>
</head>
<body>
<div class="flyer">
  <div class="bush-photo" role="img" aria-label="Lush green shrubs in a landscaped garden"></div>
  <div class="hedge-photo" role="img" aria-label="Rows of neatly trimmed green hedges along a sunlit garden path"></div>
  <div class="navy-panel"></div>

  <svg class="divider" viewBox="0 0 848 1200" aria-hidden="true">
    <line x1="0" y1="521" x2="848" y2="360" stroke="#ffffff" stroke-width="4"/>
  </svg>

  <div class="gallery-photo gallery-photo--pool" role="img" aria-label="Aerial view of a winding pool framed by hedges and lawn"></div>
  <div class="gallery-photo gallery-photo--courtyard" role="img" aria-label="Stone courtyard with trees, a fountain and a bench"></div>
  <div class="gallery-photo gallery-photo--shrubs" role="img" aria-label="Rounded shrubs lining a bright green lawn"></div>

  <div class="brand-name">CEDAR BUILDERS</div>

  <div class="section-label section-label--about">ABOUT US</div>
  <p class="section-text section-text--about">Lorem ipsum dolor sit amet, consectetur adipiscing elit, sed do eiusmod tempor incididunt ut labore et dolore magna aliqua. Quis ipsum suspendisse ultrices gravida. Risus commodo viverra maecenas accumsan lacus vel facilisis.</p>

  <div class="section-label section-label--services">OUR SERVICES</div>
  <p class="section-text section-text--services">Quis ipsum suspendisse ultrices gravida. Risus commodo viverra maecenas accumsan lacus vel facilisis. Lorem ipsum dolor sit amet, consectetur adipiscing elit, sed do eiusmod tempor incididunt ut labore et dolore magna aliqua.</p>

  <div class="contact-band">CONTACT US</div>

  <div class="contact-line contact-line--phone">
    <svg width="27" height="27" viewBox="0 0 24 24" fill="none" stroke="#0d3349" stroke-width="1.5" stroke-linejoin="round" aria-hidden="true">
      <path d="M5 2.5h3.5l1.8 4.6-2.3 1.6a12 12 0 0 0 7.3 7.3l1.6-2.3 4.6 1.8V19a2.5 2.5 0 0 1-2.5 2.5C10.3 21.5 2.5 13.7 2.5 5A2.5 2.5 0 0 1 5 2.5z"/>
    </svg>
    <span>+123 4567890</span>
  </div>

  <div class="contact-line contact-line--email">
    <svg width="28" height="22" viewBox="0 0 28 22" fill="none" stroke="#0d3349" stroke-width="1.6" aria-hidden="true">
      <rect x="1" y="1" width="26" height="20"/>
      <path d="M1 1l13 11L27 1M1 21l10-9M27 21l-10-9"/>
    </svg>
    <span>info@email.com</span>
  </div>

  <div class="contact-line contact-line--web">
    <svg width="26" height="26" viewBox="0 0 26 26" fill="none" stroke="#0d3349" stroke-width="1.5" aria-hidden="true">
      <circle cx="13" cy="13" r="12"/>
      <ellipse cx="13" cy="13" rx="5.5" ry="12"/>
      <path d="M1 13h24M3 7h20M3 19h20M13 1v24"/>
    </svg>
    <span>www.cedarbuilders.com</span>
  </div>
</div>
</body>
</html>
```